Medical Cannabis Network Website

Need a informative, detailed and functional website for a medical cannabis clinic website

check out www.velmorahealthpoint.example as competition - want better site than they have

Target Market(s)

Patients

Industry/Entity Type

Health Care

Number of Pages Required

1 page

Font styles to use
Sans Serif

Colors
cadf82
abd036
9bcb3b
3276b5
33a6d7
0392cd
f68d4e

Requirements
Must have
• Clean / Informative
• Will add additional educational content on opioid reduction
Nice to have
• like the white contrast with black/slate dividers. Green logo looks good on slate
• Check documents for ppt regarding website ideas
Should not have
• too many words

```html
<!DOCTYPE html>
<html lang="en">
<head>
<meta charset="utf-8">
<title>Velmora Medical Cannabis Network</title>
<link rel="stylesheet" href="https://fonts.googleapis.com/css2?family=Poppins:wght@300;400;500;600&display=swap">
<style>
:root{
  --green-dark:#3b8a2f;
  --green:#4f9a3a;
  --green-light:#8cc63f;
  --slate:#25292b;
  --text:#333;
  --white:#fff;
}
*{margin:0;padding:0;box-sizing:border-box}
html,body{width:1200px;height:3371px;overflow:hidden}
body{position:relative;font-family:'Poppins',sans-serif;color:var(--text);background:var(--white)}
.abs{position:absolute}
/* header */
.topbar{left:380px;top:0;width:820px;height:45px;background:var(--green-dark);border-bottom-left-radius:40px}
.topbar .phone{left:40px;top:12px;color:#fff;font-size:15px;display:flex;align-items:center;gap:8px}
.topbar .social{left:245px;top:12px;display:flex;gap:26px}
.topbar .social span{width:18px;height:18px;border-radius:50%;background:rgba(255,255,255,.85);display:block}
.book-time{left:937px;top:0;width:162px;height:45px;background:var(--green-light);color:#fff;font-size:12px;display:flex;align-items:center;justify-content:center;letter-spacing:.5px}
.brand{left:90px;top:22px;display:flex;align-items:center;gap:14px}
.brand .mark{width:62px;height:62px;border-radius:50%;background:var(--green-dark)}
.brand .name{color:var(--green-dark);font-size:14px;line-height:16px;letter-spacing:2px;font-weight:500}
.nav{top:66px;left:0;width:1200px;height:22px}
.nav a{position:absolute;font-size:13px;color:#222;text-decoration:none;letter-spacing:.3px;transform:translateX(-50%)}
.nav a.active::after{content:"";position:absolute;left:50%;top:-12px;width:8px;height:2px;background:var(--green-dark);transform:translateX(-50%)}
.infobar{left:0;top:103px;width:1200px;height:68px;background:var(--green-light)}
.info{position:absolute;top:14px;display:flex;gap:14px;color:#fff}
.info svg{width:34px;height:34px;flex:none}
.info b{display:block;font-weight:500;font-size:14px;line-height:18px}
.info small{font-size:12px;line-height:18px}
.info-sep{position:absolute;top:14px;width:1px;height:40px;background:rgba(255,255,255,.45)}
/* hero */
.hero{left:0;top:171px;width:1200px;height:634px;background:linear-gradient(180deg,#4e7fa6 0%,#7fa7c7 35%,#5f7a4a 70%,#2f4a24 100%)}
.hero-title{left:0;top:315px;width:1200px;text-align:center;color:#fff;font-weight:600}
.hero-title .l1{font-size:50px;line-height:58px}
.hero-title .l2{font-size:70px;line-height:74px}
.hero-sub{left:0;top:460px;width:1200px;text-align:center;color:#fff;font-size:22px}
.btn-book{left:521px;top:513px;width:160px;height:46px;background:var(--green-dark);color:#fff;font-size:18px;display:flex;align-items:center;justify-content:center}
.dots{left:546px;top:646px;display:flex;gap:16px}
.dots span{width:14px;height:14px;border-radius:50%;border:2px solid #fff}
.dots span:first-child{background:#fff}
/* services */
.section-title{left:0;width:1200px;text-align:center;color:var(--green-dark);font-weight:300;font-size:42px}
.card{top:939px;width:337px;height:427px;background:#fff;box-shadow:0 2px 8px rgba(0,0,0,.22)}
.card .photo{height:210px;background:linear-gradient(180deg,#dfe6ea,#b9c6cc)}
.card h3{font-weight:400;font-size:21px;line-height:28px;margin:8px 0 0 28px;color:#222}
.card p{font-size:13px;line-height:27px;color:#444;margin:12px 18px 0 30px}
.card .more{position:absolute;right:32px;bottom:-18px;width:122px;height:40px;background:var(--green-dark);color:#fff;font-size:13px;display:flex;align-items:center;justify-content:center}
.arrow{top:1140px;font-size:22px;color:#111}
/* about band */
.band{left:0;top:1528px;width:1200px;height:697px;background:linear-gradient(100deg,#2f6e22 0%,#4f8c3a 45%,#6aa251 75%,#3d7b2c 100%)}
.band-title{left:562px;top:1672px;width:560px;color:#fff;font-weight:400;font-size:40px;line-height:46px}
.band-text{left:562px;top:1786px;width:560px;color:#fff;font-size:16px;line-height:31.5px}
.btn-outline{left:564px;top:2015px;width:170px;height:50px;border:2px solid #fff;color:#fff;font-size:16px;font-weight:500;display:flex;align-items:center;justify-content:center}
/* steps */
.step{width:340px;text-align:center}
.ring{position:absolute;left:0;top:0}
.step h4{font-weight:400;font-size:19px;line-height:26px;color:#222;margin-top:180px}
.step p{font-size:16px;line-height:24px;color:#666;margin-top:14px}
/* footer */
.footer{left:0;top:2782px;width:1200px;height:589px;background:var(--slate)}
.news-title{left:121px;top:2908px;color:#fff;font-size:31px;font-weight:400}
.news-input{left:533px;top:2911px;width:404px;height:45px;background:#fff;color:#999;font-size:12px;font-style:italic;padding:14px 16px}
.news-btn{left:937px;top:2911px;width:135px;height:45px;background:var(--green-light);color:#fff;font-size:16px;display:flex;align-items:center;justify-content:center;letter-spacing:1px}
.fcol{top:3072px;color:#fff}
.fcol h5{font-weight:400;font-size:15px;letter-spacing:.5px;margin-bottom:20px}
.fcol li{list-style:none;font-size:13px;line-height:27px;color:#e6e6e6}
.fsocial{left:502px;top:3280px;display:flex;gap:10px}
.fsocial span{width:40px;height:40px;border-radius:50%;background:var(--green-light);display:block}
.copy{left:0;top:3339px;width:1200px;text-align:center;color:#ddd;font-size:11px}
</style>
</head>
<body>

<!-- header -->
<div class="abs topbar">
  <div class="abs phone">
    <svg width="16" height="16" viewBox="0 0 24 24"><path fill="#fff" d="M6.6 10.8a15 15 0 0 0 6.6 6.6l2.2-2.2c.3-.3.7-.4 1-.2 1.1.4 2.3.6 3.6.6.6 0 1 .4 1 1V20c0 .6-.4 1-1 1A17 17 0 0 1 3 4c0-.6.4-1 1-1h3.5c.6 0 1 .4 1 1 0 1.3.2 2.5.6 3.6.1.3 0 .7-.2 1z"/></svg>
    +1 555-014-2290
  </div>
  <div class="abs social"><span></span><span></span><span></span><span></span><span></span></div>
</div>
<div class="abs book-time">BOOK A TIME</div>
<div class="abs brand">
  <div class="mark"></div>
  <div class="name">VELMORA<br>MEDICAL<br>CANNABIS<br>NETWORK</div>
</div>
<nav class="abs nav">
  <a class="active" style="left:454px">HOME</a>
  <a style="left:544px">ABOUT</a>
  <a style="left:641px">QUALIFY</a>
  <a style="left:768px">APPOINTMENTS</a>
  <a style="left:881px">FAQ</a>
  <a style="left:976px">CONTACT</a>
  <a style="left:1079px">NEWS</a>
</nav>
<div class="abs infobar">
  <div class="info" style="left:68px">
    <svg viewBox="0 0 24 24" fill="none" stroke="#fff" stroke-width="1.3"><path d="M12 21s-7-6.5-7-12a7 7 0 0 1 14 0c0 5.5-7 12-7 12z"/><circle cx="12" cy="9" r="2.5"/></svg>
    <div><b>Visit our Location</b><small>Find us near the park gate</small></div>
  </div>
  <div class="info-sep" style="left:355px"></div>
  <div class="info" style="left:390px">
    <svg viewBox="0 0 24 24" fill="none" stroke="#fff" stroke-width="1.3"><path d="M6.6 10.8a15 15 0 0 0 6.6 6.6l2.2-2.2 4.6 1V20A17 17 0 0 1 3 4h4.5l1 4.6z"/></svg>
    <div><b>Call Us Now</b><small>+1 555 018 734</small></div>
  </div>
  <div class="info-sep" style="left:600px"></div>
  <div class="info" style="left:614px">
    <svg viewBox="0 0 24 24" fill="none" stroke="#fff" stroke-width="1.3"><rect x="3" y="6" width="18" height="12"/><path d="M3 6l9 7 9-7"/></svg>
    <div><b>Send Email</b><small>hello@velmorahealthpoint.example</small></div>
  </div>
  <div class="info-sep" style="left:855px"></div>
  <div class="info" style="left:897px">
    <svg viewBox="0 0 24 24" fill="none" stroke="#fff" stroke-width="1.3"><circle cx="12" cy="12" r="9"/><path d="M12 7v5l3 3"/></svg>
    <div><b>Opening Hours</b><small>Mon - Fri : 8.30 to 7.00 pm</small></div>
  </div>
</div>

<!-- hero -->
<div class="abs hero" role="img" aria-label="Cannabis plants against a blue sky with clouds"></div>
<svg class="abs" style="left:0;top:725px" width="1200" height="82" viewBox="0 0 1200 82"><path fill="#fff" d="M0 82V40Q600 -10 1200 40V82Z"/></svg>
<div class="abs hero-title"><div class="l1">Velmora Medical</div><div class="l2">Cannabis Network</div></div>
<div class="abs hero-sub">Meet with one of our marijuana doctors</div>
<div class="abs btn-book">BOOK NOW</div>
<div class="abs dots"><span></span><span></span><span></span><span></span></div>

<!-- services -->
<h2 class="abs section-title" style="top:852px">Only Specialized Marijuana Doctor Clinic</h2>
<div class="abs arrow" style="left:30px">&#9666;</div>
<div class="abs arrow" style="left:1156px">&#9656;</div>

<div class="abs card" style="left:79px">
  <div class="photo" role="img" aria-label="Doctor consulting an older patient"></div>
  <h3>No Qualification? No Fee.</h3>
  <p>Lorem ipsum dolor sit amet, consectetur adipiscing elit, sed do eiusmod tempor incididunt ut labore et dolore magna aliqua</p>
  <div class="more">READ MORE</div>
</div>
<div class="abs card" style="left:431px">
  <div class="photo" role="img" aria-label="Physician with stethoscope in a clinic"></div>
  <h3>Qualified Physicians</h3>
  <p>Lorem ipsum dolor sit amet, consectetur adipiscing elit, sed do eiusmod tempor incididunt ut labore et dolore magna aliqua</p>
  <div class="more">READ MORE</div>
</div>
<div class="abs card" style="left:785px">
  <div class="photo" role="img" aria-label="Doctor speaking with a patient"></div>
  <h3 style="margin-top:16px">Convenience</h3>
  <p>Lorem ipsum dolor sit amet, consectetur adipiscing elit, sed do eiusmod tempor incididunt ut labore</p>
  <div class="more">READ MORE</div>
</div>

<!-- about band -->
<div class="abs band" role="img" aria-label="Green field with a person enjoying the outdoors"></div>
<svg class="abs" style="left:0;top:2160px" width="1200" height="70" viewBox="0 0 1200 70"><path fill="#fff" d="M0 70V60Q600 -20 1200 60V70Z"/></svg>
<h2 class="abs band-title">Velmora Medical Cannabis Network</h2>
<p class="abs band-text">Lorem ipsum dolor sit amet, consectetur adipiscing elit, sed do eiusmod tempor incididunt ut labore et dolore magna aliqua. Ut enim ad minim veniam, quis nostrud exercitation ullamco laboris nisi ut aliquip ex ea commodo consequat. Duis aute irure dolor in reprehenderit in voluptate velit esse cillum dolore eu fugiat nulla pariatur.</p>
<div class="abs btn-outline">READ MORE</div>

<!-- steps -->
<h2 class="abs section-title" style="top:2276px">3 STEPS TO GET YOUR CARD</h2>

<div class="abs step" style="left:75px;top:2372px">
  <svg class="ring" style="left:95px" width="160" height="160" viewBox="0 0 160 160">
    <circle cx="80" cy="78" r="72" fill="none" stroke="#ccc" stroke-width="5"/>
    <path d="M80 6A72 72 0 0 1 140 118" fill="none" stroke="var(--green-light)" stroke-width="5"/>
    <rect x="62" y="58" width="30" height="38" fill="var(--green-light)"/>
    <path d="M70 86l24-24 4 4-24 24h-4z" fill="#fff"/>
    <circle cx="130" cy="130" r="20" fill="var(--green-dark)"/>
    <text x="130" y="136" text-anchor="middle" fill="#fff" font-size="16" font-family="Poppins,sans-serif">01</text>
  </svg>
  <h4>1. Complete your application<br>here online</h4>
  <p>Sed ut perspiciatis unde omnis<br>iste natus error sit voluptatem<br>accusantium laudantium</p>
</div>

<div class="abs step" style="left:428px;top:2372px">
  <svg class="ring" style="left:95px" width="160" height="160" viewBox="0 0 160 160">
    <circle cx="80" cy="78" r="72" fill="none" stroke="#ccc" stroke-width="5"/>
    <path d="M80 6A72 72 0 0 1 152 78" fill="none" stroke="var(--green-light)" stroke-width="5"/>
    <rect x="62" y="66" width="36" height="28" rx="3" fill="var(--green-light)"/>
    <rect x="72" y="60" width="16" height="8" fill="none" stroke="var(--green-light)" stroke-width="3"/>
    <rect x="74" y="76" width="12" height="4" fill="#fff"/>
    <circle cx="80" cy="20" r="20" fill="var(--green-dark)"/>
    <text x="80" y="26" text-anchor="middle" fill="#fff" font-size="16" font-family="Poppins,sans-serif">02</text>
  </svg>
  <h4>2. Get a Doctor's<br>Recommendation</h4>
  <p>Sed ut perspiciatis unde omnis<br>iste natus error sit voluptatem<br>accusantium laudantium</p>
</div>

<div class="abs step" style="left:783px;top:2372px">
  <svg class="ring" style="left:95px" width="160" height="160" viewBox="0 0 160 160">
    <circle cx="80" cy="78" r="72" fill="none" stroke="#ccc" stroke-width="5"/>
    <path d="M80 6A72 72 0 0 1 136 33" fill="none" stroke="var(--green-light)" stroke-width="5"/>
    <rect x="62" y="66" width="36" height="30" rx="3" fill="var(--green-light)"/>
    <rect x="72" y="59" width="16" height="9" fill="none" stroke="var(--green-light)" stroke-width="3"/>
    <path d="M77 73h6v5h5v6h-5v5h-6v-5h-5v-6h5z" fill="#fff"/>
    <circle cx="136" cy="50" r="20" fill="var(--green-dark)"/>
    <text x="136" y="56" text-anchor="middle" fill="#fff" font-size="16" font-family="Poppins,sans-serif">03</text>
  </svg>
  <h4>3. Getting Medical<br>Marijuana</h4>
  <p>Sed ut perspiciatis unde omnis<br>iste natus error sit voluptatem<br>accusantium laudantium</p>
</div>

<!-- footer -->
<footer class="abs footer"></footer>
<svg class="abs" style="left:0;top:2780px" width="1200" height="60" viewBox="0 0 1200 60"><path fill="#fff" d="M0 0H1200V4Q600 100 0 4Z"/></svg>
<h3 class="abs news-title">Subscribe Our Newsletter</h3>
<div class="abs news-input">Enter Your Email Id</div>
<div class="abs news-btn">Subscribe</div>

<div class="abs fcol" style="left:117px">
  <h5>QUICK LINKS</h5>
  <ul><li>Home</li><li>About</li><li>Qualify</li><li>Appointments</li></ul>
</div>
<div class="abs fcol" style="left:337px;top:3112px">
  <ul><li>Faq</li><li>Contact</li><li>News</li></ul>
</div>
<div class="abs fcol" style="left:551px">
  <h5>OTHER LINKS</h5>
  <ul><li>Terms &amp; Policy</li><li>Sitemap</li><li>Policy</li></ul>
</div>
<div class="abs fcol" style="left:831px">
  <h5>CONTACT US</h5>
  <ul><li>48 Fernbrook Lane, Larkhaven, CA</li><li>90000</li><li>(555) 013-4471</li><li>hello@velmorahealthpoint.example</li></ul>
</div>

<div class="abs fsocial"><span></span><span></span><span></span><span></span></div>
<div class="abs copy">© Copyrights 2019 Velmora Health Point All Rights Reserved</div>

</body>
</html>
```